IT Company that provides secure IT solutions and services to our customers

We need business cards and a logo for a new IT Solutions company just created based in Kuala Lumpur, Malaysia. But will also be serving other countries in the region. We provide secure data, voice solutions on mobile platforms. Our first offering is encrypted voice and data solutions for ZUN, Pellovan, Quillet and Frondmoss devices.

Target Market(s)

large organizations Govt, Police, Defence, Anti-corruption, Legal, highly regulated industries such as Health-care, Financial, Banking, Insurance,

Industry/Entity Type

Information Technology

Contact Information for Business Card

VorlexIT (Logo - colour is ORVA blue)Rashid Nawfal Managing Director Kryption IT Sdn. Bhd.3rd Floor, Block C, Wisma LPN,No.14 Jalan Seri Hamzani,58410, Kuala LumpurMalaysia

Font styles to use
Sans Serif

Colors
3176b5
ec1f27
fbed22

Requirements
Must have
• VorlexIT all in Blue like ORVA blue. A logo design perhaps a play of VI, K with a dangling T (colour can be any)
Nice to have
• I want a clean crisp card, not too busy, easy to read.

```html
<!DOCTYPE html>
<html lang="en">
<head>
<meta charset="utf-8">
<title>VorlexIT Business Card</title>
<link rel="stylesheet" href="https://fonts.googleapis.com/css2?family=Roboto+Condensed:wght@400;700&display=swap">
<style>
  :root {
    --brand-blue: #3176b5;
    --brand-red: #ec1f27;
    --paper: #ffffff;
    --backdrop: #e8e1d4;
    --card-shadow: 0 2px 6px rgba(60, 40, 20, 0.25);
  }
  * { margin: 0; padding: 0; box-sizing: border-box; }
  html, body {
    width: 939px; height: 1200px; overflow: hidden;
    background: var(--backdrop);
    font-family: "Roboto Condensed", "Arial Narrow", sans-serif;
  }
  .canvas { position: relative; width: 939px; height: 1200px; }

  .card {
    position: absolute; width: 744px; height: 448px;
    box-shadow: var(--card-shadow); overflow: hidden;
  }
  .card-front { left: 88px; top: 100px; background: var(--paper); }
  .card-back { left: 91px; top: 646px; background: var(--brand-blue); }

  /* front */
  .front-band {
    position: absolute; left: 0; right: 0; top: 187px; bottom: 0;
    background: var(--brand-blue);
    border-top: 5px solid var(--brand-red);
  }
  .brand {
    position: absolute; display: flex; align-items: center; gap: 12px;
    font-weight: 700; line-height: 1;
  }
  .brand-front { left: 46px; top: 72px; color: var(--brand-blue); font-size: 46px; }
  .brand-front .brand-square { width: 26px; height: 26px; background: var(--brand-blue); }
  .brand-back { right: 70px; top: 94px; color: var(--paper); font-size: 38px; }
  .brand-back .brand-square { width: 22px; height: 22px; background: var(--brand-red); }

  .person { position: absolute; right: 87px; top: 98px; text-align: right; color: var(--brand-blue); }
  .person-name { font-weight: 700; font-size: 26px; line-height: 34px; }
  .person-title { font-weight: 400; font-size: 25px; line-height: 36px; }

  .contacts { position: absolute; right: 78px; top: 219px; list-style: none; color: var(--paper); }
  .contacts li {
    display: flex; justify-content: flex-end; align-items: center; gap: 10px;
    font-size: 22px; height: 31px;
  }
  .contacts svg { width: 22px; height: 22px; fill: none; stroke: var(--brand-red); stroke-width: 1.8; }

  .address {
    position: absolute; right: 78px; top: 350px;
    display: flex; align-items: center; gap: 12px;
    color: var(--paper); font-size: 22px; line-height: 32px; text-align: right;
  }
  .address svg { width: 22px; height: 34px; }

  /* back */
  .offer { position: absolute; left: 93px; top: 98px; color: var(--paper); font-size: 28px; line-height: 38px; }
  .offer-heading { font-weight: 700; }
  .platforms { position: absolute; left: 98px; top: 284px; color: var(--paper); font-size: 27px; line-height: 37px; }
</style>
</head>
<body>
<main class="canvas">

  <section class="card card-front">
    <div class="front-band"></div>

    <div class="brand brand-front"><span class="brand-square"></span><span>VorlexIT</span></div>

    <div class="person">
      <p class="person-name">Rashid Nawfal</p>
      <p class="person-title">Managing Director</p>
    </div>

    <ul class="contacts">
      <li>Phone number
        <svg viewBox="0 0 24 24"><path d="M17 3c2 2 2 6 0 10s-6 8-10 8" stroke-linecap="round"/><path d="M15 3h4M5 21v-3"/></svg>
      </li>
      <li>Mobile number
        <svg viewBox="0 0 24 24"><rect x="6" y="3" width="12" height="18" rx="1.5"/><line x1="10" y1="18" x2="14" y2="18"/></svg>
      </li>
      <li>email
        <svg viewBox="0 0 24 24"><rect x="2" y="6" width="20" height="12"/><path d="M2 6l10 7 10-7"/></svg>
      </li>
      <li>www
        <svg viewBox="0 0 24 24"><circle cx="12" cy="12" r="9"/><ellipse cx="12" cy="12" rx="4" ry="9"/><line x1="3" y1="12" x2="21" y2="12"/></svg>
      </li>
    </ul>

    <div class="address">
      <p>Sdn. Bhd.3rd Floor, Block C, Wisma LPN,No.14<br>Jalan Seri Hamzani, 58410, Kuala Lumpur, Malaysia</p>
      <svg viewBox="0 0 22 34"><path d="M11 1C5.5 1 1 5.3 1 10.8 1 18 11 33 11 33s10-15 10-22.2C21 5.3 16.5 1 11 1z" fill="var(--brand-red)"/><circle cx="11" cy="11" r="4" fill="var(--brand-blue)"/></svg>
    </div>
  </section>

  <section class="card card-back">
    <div class="offer">
      <p class="offer-heading">We provide:</p>
      <p>Secure data,</p>
      <p>Voice solutions on mobile platforms</p>
    </div>

    <div class="brand brand-back"><span class="brand-square"></span><span>VorlexIT</span></div>

    <div class="platforms">
      <p>Encrypted voice and data solutions for</p>
      <p>ZUN, Pellovan, Quillet and Frondmoss devices</p>
    </div>
  </section>

</main>
</body>
</html>
```